Business Card Design

We currently have a business card design for our main business 'Lantern Wallcover"
We are reasonably happy with our current design for Lantern Wallcover business card (black damask patterned wallpaper in background white simplistic font with white chandelier (see logo on website). www.lanternwallcover.com.au

We are considering whether its in our best interest to have a separate business card OR a double sided card to promote our secondary business 'Quill Glow'. We are open to either a double-sided card with one business on each side OR a double sided card for each business. With contact info on the back of each.

We need a new snazzy design for 'Quill Glow' our custom made lampshades from which we craft from our wallpaper designs. We had an idea that we could use the top swatch shown on this link below as the pattern in the background (Orange/black) geometric triangles.
http://www.lanternwallcover.com.au/product_info.php?products_id=1086

For the quill glow Font we would be happy with something similar to Lantern Wallcover but perhaps a little more handmade/arty slant.
Below another link shows you a few of our lampshades
http://www.lanternwallcover.com.au/index.php?cPath=10

For Quill Glow I think we also need the quote under in smaller font
"Custom-Made Wallpaper Lampshades"

Target Market(s)

Quill Glow will be for the Young Funky Apartment Dwellers, Young Families Styling Home Decor and Kids Rooms. It also attracts small business owners doing shop-fits.

Industry/Entity Type

Business

Contact Information for Business Card

We need to incorporate our sister business to the back side of our business card. I am also open to having two different business cards if designers think this will not be possible.
We need the same contact info, different logo.
ABN: 47 302 916 854
Email: sales@lanternwallcover.com.au
Postal Address: PO Box 793, Larkfield VIC 3389
Website: http://www.lanternwallcover.com.au

Requirements
Must have
• A hand-made arty appeal for Quill Glow
Was unable to get sliders to work for the look and feel so below is the best list from the above:
Bold, Playful, Modern, Personable, Colorful, Upmarket.
Nice to have
• We love the bold contrasting colors. Colors chosen for our website were Orange, Blue and Duck Egg Bright Blue!

```html
<!DOCTYPE html>
<html lang="en">
<head>
<meta charset="utf-8">
<title>Lantern Wallcover &amp; Quill Glow — Business Cards</title>
<link rel="stylesheet" href="https://fonts.googleapis.com/css2?family=Ubuntu:wght@400&family=Roboto+Condensed:wght@400&display=swap">
<style>
  :root {
    --canvas-bg: #e8e5e1;
    --card-black: #0b0b0c;
    --damask-light: #4a4a52;
    --damask-dark: #1b1b20;
    --card-plum: #2b2733;
    --pill-white: #ffffff;
    --pill-ink: #2a2833;
    --text-white: #ffffff;
    --tri-pink: #ef9aa0;
    --tri-yellow: #d9dc55;
    --tri-grey: #b5b5b8;
    --tri-slate: #4a4d55;
    --tri-orange: #ec9a3c;
  }
  * { margin: 0; padding: 0; box-sizing: border-box; }
  html, body { width: 1200px; height: 900px; overflow: hidden; }
  body { background: var(--canvas-bg); position: relative; }

  .card {
    position: absolute;
    width: 704px;
    height: 398px;
    border-radius: 22px;
    overflow: hidden;
    box-shadow: 0 6px 16px rgba(0,0,0,0.25);
  }
  .card--lantern { left: 88px; top: 35px; background: var(--card-black); }
  .card--quill { left: 393px; top: 465px; background: var(--card-plum); }

  .card__art { position: absolute; inset: 0; width: 100%; height: 100%; }

  .brand-pill {
    position: absolute;
    background: var(--pill-white);
    border: 3px solid var(--pill-ink);
    border-radius: 34px;
    display: flex;
    align-items: center;
    justify-content: center;
    font-family: "Ubuntu", sans-serif;
    font-size: 41px;
    color: var(--pill-ink);
    white-space: nowrap;
    letter-spacing: -0.3px;
  }
  .card--lantern .brand-pill { left: 138px; top: 72px; width: 379px; height: 65px; }
  .card--quill .brand-pill { left: 239px; top: 62px; width: 318px; height: 66px; }

  .tagline {
    position: absolute;
    font-family: "Ubuntu", sans-serif;
    font-size: 14px;
    line-height: 19px;
    color: var(--text-white);
  }
  .card--lantern .tagline { right: 571px; top: 75px; text-align: right; }
  .card--quill .tagline { left: 572px; top: 68px; text-align: left; }

  .contact {
    position: absolute;
    list-style: none;
    font-family: "Roboto Condensed", sans-serif;
    font-size: 14.5px;
    line-height: 27px;
    color: var(--text-white);
    white-space: nowrap;
  }
  .card--lantern .contact { left: 34px; top: 262px; }
  .card--quill .contact { left: 390px; top: 266px; }
</style>
</head>
<body>

  <section class="card card--lantern">
    <svg class="card__art" viewBox="0 0 704 398" preserveAspectRatio="none">
      <defs>
        <radialGradient id="damask-tone" cx="55%" cy="45%" r="70%">
          <stop offset="0" stop-color="var(--damask-light)"/>
          <stop offset="1" stop-color="var(--damask-dark)"/>
        </radialGradient>
      </defs>
      <rect width="704" height="398" fill="url(#damask-tone)" role="img" aria-label="Grey damask wallpaper pattern"/>
      <path d="M0 0 H182 C260 10 290 120 300 200 C310 290 300 360 322 398 H0 Z" fill="var(--card-black)"/>
    </svg>
    <p class="tagline">Custom-Made<br>Wallpaper<br>Lampshades</p>
    <div class="brand-pill">Lantern Wallcover</div>
    <ul class="contact">
      <li>&nbsp;ABN : 47 302 916 854</li>
      <li>Email : sales@lanternwallcover.com.au</li>
      <li>Add &nbsp;: PO Box 793, Larkfield VIC 3389</li>
      <li>Web : http://www.lanternwallcover.com.au</li>
    </ul>
  </section>

  <section class="card card--quill">
    <svg class="card__art" viewBox="0 0 704 398" preserveAspectRatio="none">
      <defs>
        <linearGradient id="triangle-tone" x1="0" y1="0" x2="1" y2="1">
          <stop offset="0" stop-color="var(--tri-slate)"/>
          <stop offset="0.3" stop-color="var(--tri-pink)"/>
          <stop offset="0.55" stop-color="var(--tri-grey)"/>
          <stop offset="0.78" stop-color="var(--tri-yellow)"/>
          <stop offset="1" stop-color="var(--tri-orange)"/>
        </linearGradient>
      </defs>
      <rect width="704" height="398" fill="url(#triangle-tone)" role="img" aria-label="Colourful geometric triangle wallpaper pattern in pink, yellow, grey, slate and orange"/>
      <path d="M507 0 C540 60 520 120 470 180 C400 260 360 330 367 398 H704 V0 Z" fill="var(--card-plum)"/>
    </svg>
    <div class="brand-pill">Quill Glow</div>
    <p class="tagline">Custom-Made<br>Wallpaper<br>Lampshades</p>
    <ul class="contact">
      <li>&nbsp;ABN : 47 302 916 854</li>
      <li>Email : sales@lanternwallcover.com.au</li>
      <li>Add &nbsp;: PO Box 793, Larkfield VIC 3389</li>
      <li>Web : http://www.lanternwallcover.com.au</li>
    </ul>
  </section>

</body>
</html>
```